Email Sig, Letterhead, Business Card Design

Need a stationary package including email signature, letterhead/envelope, and business card design incorporating our new logo.

```html
<!DOCTYPE html>
<html lang="en">
<head>
<meta charset="utf-8">
<title>Marlow Engineering – Stationery Package</title>
<link href="https://fonts.googleapis.com/css2?family=Cinzel:wght@600&family=Exo+2:wght@400;500&family=Roboto:wght@400;700&family=Dancing+Script&display=swap" rel="stylesheet">
<style>
:root{
  --blue:#1d5fa6;
  --blue-deep:#134b8a;
  --orange:#e0552a;
  --board:#262626;
  --stage:#3b3b3b;
  --label:#8a8a8a;
  --ink:#2c2c2c;
  --paper:#ffffff;
  --steel:#5a5a5a;
  --art-top:#efc2ae;
  --art-bottom:#b9cbe0;
  --serif:"Cinzel",Georgia,serif;
  --sans:"Exo 2",Arial,sans-serif;
  --body:"Roboto",Arial,sans-serif;
}
*{box-sizing:border-box;margin:0;padding:0}
html,body{width:702px;height:1200px;overflow:hidden;background:var(--board)}
.board{position:relative;width:702px;height:1200px;background:var(--board);font-family:var(--sans)}
.stage{position:absolute;left:0;top:0;width:702px;height:458px;background:var(--stage)}
.label{position:absolute;font-family:var(--sans);font-size:13px;color:var(--label);letter-spacing:.3px}

/* brand lockup */
.brand{position:absolute;text-align:center}
.brand-dot{display:block;margin:0 auto 4px;border-radius:50%;background:var(--blue)}
.brand-name{font-family:var(--serif);font-weight:600;color:var(--orange);white-space:nowrap;line-height:1}
.brand-addr{font-family:Georgia,serif;color:var(--blue);white-space:nowrap;line-height:1.3;font-weight:bold}
.brand-reg{display:flex;align-items:center;gap:3px;font-family:Georgia,serif;color:var(--orange);letter-spacing:.6px;white-space:nowrap;line-height:1}
.brand-reg::before,.brand-reg::after{content:"";flex:1;height:.5px;background:currentColor}

/* contacts */
.contacts{position:absolute;list-style:none;color:var(--ink)}
.contacts li{display:flex;align-items:center;white-space:nowrap}
.contacts svg{flex:none}

/* decorative emblem area placeholder */
.emblem-art{position:absolute;background:linear-gradient(180deg,var(--art-top),var(--art-bottom))}

/* business card front */
.card{position:absolute;width:308px;height:176px;overflow:hidden}
.card-front{background:var(--paper)}
.card-front .brand{left:10px;top:10px;width:100px}
.card-front .brand-dot{width:18px;height:18px}
.card-front .brand-name{font-size:9.6px}
.card-front .brand-addr{font-size:3.4px}
.card-front .brand-reg{font-size:2.8px}
.person-name{font-family:var(--serif);font-weight:600;color:var(--blue);white-space:nowrap;line-height:1}
.person-role{font-family:var(--sans);color:var(--orange);white-space:nowrap;display:flex;align-items:flex-end;gap:2px;line-height:1}
.person-role::after{content:"";height:.6px;background:linear-gradient(90deg,var(--blue),transparent);flex:1;margin-bottom:1px}
.card-front .person{position:absolute;left:12px;top:86px;width:178px}
.card-front .person-name{font-size:10.4px}
.card-front .person-role{font-size:8px;margin-top:3px}
.card-front .contacts{left:12px;top:121px;font-size:6.6px}
.card-front .contacts li{height:10px;gap:5px}
.card-front .emblem-art{left:196px;top:0;width:112px;height:171px}
.band-orange{position:absolute;left:0;right:0;bottom:0;background:var(--orange)}
.card-front .band-orange{height:5px}

/* business card back */
.card-back{background:var(--blue)}
.card-back .pattern{position:absolute;inset:0;background:linear-gradient(135deg,#2069b3,#1a5ea4)}
.card-back .brand{left:80px;top:42px;width:148px}
.card-back .brand-dot{width:32px;height:32px;margin-bottom:8px;background:none;border:2.5px solid #fff}
.card-back .brand-name{font-size:14px;color:#fff}
.card-back .brand-addr{font-size:5px;color:#fff}
.card-back .brand-reg{font-size:4.2px;color:#fff;margin-top:2px}

.staged .card{transform:scale(.9);transform-origin:0 0;box-shadow:0 6px 14px rgba(0,0,0,.45)}
.stage-brand{left:22px;top:336px;width:128px}
.stage-brand .brand-dot{width:40px;height:40px;background:none;border:3px solid #8d8d8d;margin-bottom:8px}
.stage-brand .brand-name{font-size:13.4px;color:#9a9a9a}
.stage-brand .brand-addr{font-size:4.6px;color:#9a9a9a}
.stage-brand .brand-reg{font-size:3.8px;color:#9a9a9a;margin-top:1px}

/* letterhead */
.letterhead{position:absolute;left:27px;top:729px;width:282px;height:403px;overflow:hidden;background:linear-gradient(160deg,#f3f3f3,#dadada)}
.letterhead .brand{left:81px;top:15px;width:120px}
.letterhead .brand-dot{width:34px;height:34px;margin-bottom:9px}
.letterhead .brand-name{font-size:11.2px}
.letterhead .brand-addr{font-size:4px}
.letterhead .brand-reg{font-size:3.4px}
.addressee{position:absolute;left:29px;top:117px;font-family:var(--body)}
.addressee-name{font-size:8.6px;font-weight:700;color:var(--blue)}
.addressee-role{font-size:6px;font-weight:700;color:var(--orange)}
.letter-date{position:absolute;right:29px;top:119px;font-family:var(--body);font-size:4.8px;font-weight:700;color:var(--ink)}
.letter-body{position:absolute;left:29px;top:140px;width:226px;font-family:var(--body);font-size:4.5px;line-height:8.7px;color:var(--ink)}
.letter-body p{margin-bottom:8.7px}
.sign{position:absolute;left:29px;top:266px;font-family:var(--body)}
.sign-script{font-family:"Dancing Script",cursive;font-size:10px;color:var(--ink)}
.sign-name{font-size:5.2px;font-weight:700;color:var(--ink);margin-top:3px}
.sign-role{font-size:4.6px;font-weight:700;color:var(--orange);margin-top:2px}
.letter-band{position:absolute;left:0;right:0;bottom:0;height:61px;background:var(--blue)}
.letterhead .emblem-art{left:194px;top:260px;width:88px;height:143px}
.letterhead .contacts{left:28px;top:352px;font-size:6.8px;color:#fff}
.letterhead .contacts li{height:10px;gap:5px}

/* envelope */
.env-back{position:absolute;left:372px;top:728px;width:304px;height:185px;background:#e9e9ea;border-radius:14px 14px 0 0;overflow:hidden}
.env-flap{position:absolute;left:0;top:0;width:100%;height:34px;background:var(--orange);border-radius:14px 14px 0 0}
.env-front{position:absolute;left:339px;top:798px;width:305px;height:152px;background:linear-gradient(160deg,#ededed,#dedede);overflow:hidden;box-shadow:0 2px 8px rgba(0,0,0,.3)}
.env-front .brand{left:14px;top:12px;width:84px}
.env-front .brand-dot{width:22px;height:22px;margin-bottom:6px}
.env-front .brand-name{font-size:8.4px}
.env-front .brand-addr{font-size:2.8px}
.env-front .brand-reg{font-size:2.4px}
.env-front .contacts{left:12px;top:99px;font-size:5.2px}
.env-front .contacts li{height:7.6px;gap:4px}
.address-lines{position:absolute;left:164px;top:95px;width:117px}
.address-lines span{display:block;height:13px;border-bottom:.6px solid #555}
.env-front .band-orange{height:4px}

/* email signature */
.signature{position:absolute;left:339px;top:987px;width:313px;height:158px;background:var(--paper);overflow:hidden}
.signature .brand{left:12px;top:32px;width:122px}
.signature .brand-dot{width:34px;height:34px;margin-bottom:14px}
.signature .brand-name{font-size:11.6px}
.signature .brand-addr{font-size:3.8px}
.signature .brand-reg{font-size:3.2px}
.sig-divider{position:absolute;left:144px;top:18px;width:.6px;height:120px;background:#d8d8d8}
.signature .person{position:absolute;left:154px;top:44px;width:159px}
.signature .person-name{font-size:10.6px}
.signature .person-role{font-size:8px;margin-top:3px}
.signature .contacts{left:154px;top:71px;font-size:7px}
.signature .contacts li{height:10.6px;gap:5px}
.signature .band-orange{height:5px}
</style>
</head>
<body>
<svg width="0" height="0" style="position:absolute" aria-hidden="true">
  <symbol id="ico-phone" viewBox="0 0 10 10"><circle cx="5" cy="5" r="5" fill="currentColor"/><path d="M3.3 2.6c.3-.2.6-.2.8.1l.5.8c.1.3 0 .5-.2.7l-.3.2c.3.7.8 1.2 1.5 1.5l.2-.3c.2-.2.4-.3.7-.2l.8.5c.3.2.3.5.1.8-.6.8-1.5.7-2.6 0S2.8 4.8 2.9 3.7c0-.5.1-.8.4-1.1z" fill="#fff"/></symbol>
  <symbol id="ico-mail" viewBox="0 0 10 10"><circle cx="5" cy="5" r="5" fill="currentColor"/><rect x="2.6" y="3.3" width="4.8" height="3.4" rx=".4" fill="#fff"/><path d="M2.8 3.6 5 5.3l2.2-1.7" stroke="currentColor" stroke-width=".6" fill="none"/></symbol>
  <symbol id="ico-web" viewBox="0 0 10 10"><circle cx="5" cy="5" r="5" fill="currentColor"/><circle cx="5" cy="5" r="2.5" fill="none" stroke="#fff" stroke-width=".6"/><path d="M2.5 5h5M5 2.5v5" stroke="#fff" stroke-width=".6"/></symbol>
  <symbol id="ico-pin" viewBox="0 0 10 10"><circle cx="5" cy="5" r="5" fill="currentColor"/><path d="M5 2.2a2 2 0 0 1 2 2c0 1.5-2 3.6-2 3.6S3 5.7 3 4.2a2 2 0 0 1 2-2z" fill="#fff"/><circle cx="5" cy="4.2" r=".7" fill="currentColor"/></symbol>
</svg>

<main class="board">

  <section class="stage staged">
    <div class="card card-back" style="left:112px;top:30px">
      <div class="pattern" role="img" aria-label="Repeating brand pattern area"></div>
      <div class="brand">
        <span class="brand-dot"></span>
        <div class="brand-name">Marlow Engineering</div>
        <div class="brand-addr">41520 CEDAR RIDGE LANE, KINGSFORD, TEXAS 77590</div>
        <div class="brand-reg">TBPE FIRM REGISTRATION F-4418</div>
      </div>
    </div>

    <div class="card card-front" style="left:366px;top:188px">
      <div class="brand">
        <span class="brand-dot"></span>
        <div class="brand-name">Marlow Engineering</div>
        <div class="brand-addr">41520 CEDAR RIDGE LANE, KINGSFORD, TEXAS 77590</div>
        <div class="brand-reg">TBPE FIRM REGISTRATION F-4418</div>
      </div>
      <div class="person">
        <div class="person-name">Daniel Reyes</div>
        <div class="person-role">Managing Director</div>
      </div>
      <ul class="contacts">
        <li><svg width="7" height="7" style="color:var(--blue)"><use href="#ico-phone"/></svg>+444 (555) 010-2233</li>
        <li><svg width="7" height="7" style="color:var(--blue)"><use href="#ico-mail"/></svg>hello@marlowmail.com</li>
        <li><svg width="7" height="7" style="color:var(--blue)"><use href="#ico-web"/></svg>www.marlowsite.com</li>
        <li><svg width="7" height="7" style="color:var(--blue)"><use href="#ico-pin"/></svg>880 Quarry Hill Rd, PO Box 7 Ashby</li>
      </ul>
      <div class="emblem-art" role="img" aria-label="Large decorative brand artwork area"></div>
      <div class="band-orange"></div>
    </div>

    <div class="brand stage-brand">
      <span class="brand-dot"></span>
      <div class="brand-name">Marlow Engineering</div>
      <div class="brand-addr">41520 CEDAR RIDGE LANE, KINGSFORD, TEXAS 77590</div>
      <div class="brand-reg">TBPE FIRM REGISTRATION F-4418</div>
    </div>
    <p class="label" style="left:20px;top:426px">Businesscard Mockup</p>
  </section>

  <div class="card card-front" style="left:26px;top:493px">
    <div class="brand">
      <span class="brand-dot"></span>
      <div class="brand-name">Marlow Engineering</div>
      <div class="brand-addr">41520 CEDAR RIDGE LANE, KINGSFORD, TEXAS 77590</div>
      <div class="brand-reg">TBPE FIRM REGISTRATION F-4418</div>
    </div>
    <div class="person">
      <div class="person-name">Daniel Reyes</div>
      <div class="person-role">Managing Director</div>
    </div>
    <ul class="contacts">
      <li><svg width="7" height="7" style="color:var(--blue)"><use href="#ico-phone"/></svg>+444 (555) 010-2233</li>
      <li><svg width="7" height="7" style="color:var(--blue)"><use href="#ico-mail"/></svg>hello@marlowmail.com</li>
      <li><svg width="7" height="7" style="color:var(--blue)"><use href="#ico-web"/></svg>www.marlowsite.com</li>
      <li><svg width="7" height="7" style="color:var(--blue)"><use href="#ico-pin"/></svg>880 Quarry Hill Rd, PO Box 7 Ashby</li>
    </ul>
    <div class="emblem-art" role="img" aria-label="Large decorative brand artwork area"></div>
    <div class="band-orange"></div>
  </div>
  <p class="label" style="left:27px;top:683px">Businesscard front</p>

  <div class="card card-back" style="left:365px;top:493px">
    <div class="pattern" role="img" aria-label="Repeating brand pattern area"></div>
    <div class="brand">
      <span class="brand-dot"></span>
      <div class="brand-name">Marlow Engineering</div>
      <div class="brand-addr">41520 CEDAR RIDGE LANE, KINGSFORD, TEXAS 77590</div>
      <div class="brand-reg">TBPE FIRM REGISTRATION F-4418</div>
    </div>
  </div>
  <p class="label" style="left:364px;top:683px">Businesscard Back</p>

  <article class="letterhead">
    <div class="brand">
      <span class="brand-dot"></span>
      <div class="brand-name">Marlow Engineering</div>
      <div class="brand-addr">41520 CEDAR RIDGE LANE, KINGSFORD, TEXAS 77590</div>
      <div class="brand-reg">TBPE FIRM REGISTRATION F-4418</div>
    </div>
    <div class="addressee">
      <div class="addressee-name">Clara Benton</div>
      <div class="addressee-role">Designer</div>
    </div>
    <div class="letter-date">Date : 25 September, 2030</div>
    <div class="letter-body">
      <p>Lorem ipsum dolor sit amet, consectetur adipisicing elit, sed do eiusmod tempor incididunt ut labore et dolore magna aliqua. Ut enim ad minim veniam, quis nostrud exercitation ullamco laboris nisi ut aliquip ex ea commodo consequat.</p>
      <p>Excepteur sint occaecat cupidatat non proident, sunt in culpa qui officia deserunt mollit anim id est laborum. Sed ut perspiciatis unde omnis iste natus error sit voluptatem accusantium doloremque laudantium, totam rem aperiam, eaque ipsa quae ab illo inventore veritatis et quasi architecto beatae vitae dicta sunt explicabo. Nemo enim ipsam voluptatem quia voluptas sit aspernatur aut odit aut quia consequuntur voluptatem sequi nesciunt.</p>
      <p>Voluptatem accusantium doloremque laudantium, totam rem aperiam, eaque ipsa quae ab illo inventore veritatis et quasi architecto beatae vitae dicta sunt explicabo. Nemo enim ipsam voluptatem quia voluptas sit aspernatur aut odit aut quia consequuntur voluptatem sequi nesciunt.</p>
    </div>
    <div class="sign">
      <div class="sign-script">Martin Hale</div>
      <div class="sign-name">Martin Hale</div>
      <div class="sign-role">Manager</div>
    </div>
    <div class="letter-band"></div>
    <div class="emblem-art" role="img" aria-label="Large decorative brand artwork area"></div>
    <ul class="contacts">
      <li><svg width="7" height="7" style="color:var(--orange)"><use href="#ico-phone"/></svg>+444 (555) 010-2233</li>
      <li><svg width="7" height="7" style="color:var(--orange)"><use href="#ico-mail"/></svg>hello@marlowmail.com</li>
      <li><svg width="7" height="7" style="color:var(--orange)"><use href="#ico-web"/></svg>www.marlowsite.com</li>
      <li><svg width="7" height="7" style="color:var(--orange)"><use href="#ico-pin"/></svg>880 Quarry Hill Rd, PO Box 7 Ashby</li>
    </ul>
  </article>
  <p class="label" style="left:27px;top:1152px">Letterhead</p>

  <div class="env-back"><div class="env-flap" role="img" aria-label="Brand pattern area on envelope flap"></div></div>
  <div class="env-front">
    <div class="brand">
      <span class="brand-dot"></span>
      <div class="brand-name">Marlow Engineering</div>
      <div class="brand-addr">41520 CEDAR RIDGE LANE, KINGSFORD, TEXAS 77590</div>
      <div class="brand-reg">TBPE FIRM REGISTRATION F-4418</div>
    </div>
    <ul class="contacts">
      <li><svg width="5" height="5" style="color:var(--blue)"><use href="#ico-phone"/></svg>+444 (555) 010-2233</li>
      <li><svg width="5" height="5" style="color:var(--blue)"><use href="#ico-mail"/></svg>hello@marlowmail.com</li>
      <li><svg width="5" height="5" style="color:var(--blue)"><use href="#ico-web"/></svg>www.marlowsite.com</li>
      <li><svg width="5" height="5" style="color:var(--blue)"><use href="#ico-pin"/></svg>880 Quarry Hill Rd, PO Box 7 Ashby</li>
    </ul>
    <div class="address-lines"><span></span><span></span><span></span><span></span></div>
    <div class="band-orange"></div>
  </div>
  <p class="label" style="left:339px;top:960px">Envelope</p>

  <div class="signature">
    <div class="brand">
      <span class="brand-dot"></span>
      <div class="brand-name">Marlow Engineering</div>
      <div class="brand-addr">41520 CEDAR RIDGE LANE, KINGSFORD, TEXAS 77590</div>
      <div class="brand-reg">TBPE FIRM REGISTRATION F-4418</div>
    </div>
    <div class="sig-divider"></div>
    <div class="person">
      <div class="person-name">Daniel Reyes</div>
      <div class="person-role">Managing Director</div>
    </div>
    <ul class="contacts">
      <li><svg width="8" height="8" style="color:var(--blue)"><use href="#ico-phone"/></svg>+444 (555) 010-2233</li>
      <li><svg width="8" height="8" style="color:var(--blue)"><use href="#ico-mail"/></svg>hello@marlowmail.com</li>
      <li><svg width="8" height="8" style="color:var(--blue)"><use href="#ico-web"/></svg>www.marlowsite.com</li>
      <li><svg width="8" height="8" style="color:var(--blue)"><use href="#ico-pin"/></svg>880 Quarry Hill Rd, PO Box 7 Ashby</li>
    </ul>
    <div class="band-orange"></div>
  </div>
  <p class="label" style="left:339px;top:1153px">E-mail Signature</p>

</main>
</body>
</html>
```